Natural Skincare Product Labels Design

We are looking for a designer to create elegant but quirky, functional product labels for our natural skincare range.
The labels must reflect our brand’s values of simplicity, luxury, and the natural, handmade essence of our products.
https://www.instagram.com/tolvarenskincare
1. Key Details
Packaging Dimensions
Container Types: Transparent jars.
Sizes for Body Products:
Diameter: 64mm–68mm.
Heights: 80mm, 88mm, and 97mm (lid height: 15mm).
Sizes for Face Creams:
Diameter: 60mm.
Height: 50mm (lid height: 15mm).
Label Fit: For body products, ideally one label size to fit all jar sizes.
For the smaller face cream jars, a separate, tailored label is required.
2. Label Placement
Options include a wrapped-around label or a combination of wrapped-around and top-of-jar elements.
Transparent jars mean the label must leave space for the product to be visible (e.g., partial wrap or cutout areas).
3. Content Requirements
Product Name: Prominently displayed.
Ingredient List: Dedicated space required.
Disclaimer/Usage Instructions: Include space for this information.
4. Design Goals
Look & Feel: Simple, upmarket, and natural, with a handmade essence.
Logo Usage: Our logo is finalized and available in gold, black, and white variants. Use Josefin Bold font for the logo if adjustments are required.
Color Palette: Neutral tones (e.g., whites, blacks, golds) are preferred, with flexibility for subtle pops of color tied to each product’s main ingredient.
5. Imagery
Open to including images and colours (e.g., botanical illustrations) that highlight the main ingredient (e.g., coffee beans, turmeric root, or honeycomb). Also open to labels having a prominent colour to tie it in to the main ingredient.
Alternatively, no images can also work for a clean design.
6. Current Design Context
Our temporary design features gold leaf on top and a simple handmade side label. We’re seeking to elevate this to a more polished, cohesive design.
7. Product Line
- Body Products (Larger Jars)
Mivo Body Butter
Key Ingredients: Guarana & Cupuaçu butter (inspired by Brazil).
Note: “Mivo” is slang for “bum.”
Manuka Honey Body Butter
Key Ingredients: Manuka honey (from New Zealand) & Cupuaçu butter.
Coffee Body Scrub
Key Ingredients: Coffee and Demerara sugar.
Whipped Body Soap - Turmeric
Key Ingredients: Turmeric and Bentonite clay.
Whipped Body Soap - Banana
- Face Products (Smaller Jars)
Face Cream
Key Ingredients: Carrot Oil and Raspberry Oil.
Features natural UV protection.
Good Night Cream
Key Ingredients: Enriched with Magnesium.
Promotes relaxation and restful sleep.
8. Submission Guidelines
Flexibility: Design should allow for consistent branding across all products while accommodating the varying jar sizes and ingredient focus.
Material Considerations: Labels should complement the transparent jars and allow the product inside to remain partially visible.
Print Elements: Incorporating gold accents is a plus but should not overpower the design.
We’re excited to see your vision for a label that celebrates the natural beauty and high quality of our skincare range. Please include mockups to showcase the design in use, particularly on transparent jars of varying sizes.
women 20-50 years of age

```html
<!DOCTYPE html>
<html lang="en">
<head>
<meta charset="utf-8">
<title>Tolvaren Natural Skincare – Body Range Labels</title>
<link rel="stylesheet" href="https://fonts.googleapis.com/css2?family=Barlow+Semi+Condensed:wght@400;500;600&family=Josefin+Sans:wght@300;400&display=swap">
<style>
  :root {
    --bg: #e4e4e4;
    --ink: #2b2a2a;
    --lilac: #cdc6d4;
    --honey: #dca76a;
    --sand: #cbc2b5;
  }
  * { box-sizing: border-box; margin: 0; padding: 0; }
  html, body { width: 1200px; height: 900px; overflow: hidden; }
  body {
    background: var(--bg);
    color: var(--ink);
    font-family: "Barlow Semi Condensed", sans-serif;
  }
  .label-sheet {
    width: 1200px; height: 900px;
    display: flex; align-items: center; justify-content: center;
    gap: 24px;
  }
  .label {
    position: relative;
    width: 360px; height: 260px;
    border-radius: 10px;
    display: flex;
    overflow: hidden;
  }
  .label--mivo { background: var(--lilac); }
  .label--honey { background: var(--honey); }
  .label--coffee { background: var(--sand); }

  .label__front { position: relative; width: 270px; height: 100%; }
  .brand {
    position: absolute; left: 34px; top: 40px;
    display: flex; align-items: center; gap: 10px;
  }
  .brand__dot { width: 10px; height: 10px; border-radius: 50%; background: var(--ink); }
  .brand__text { display: flex; flex-direction: column; }
  .brand__name {
    font-family: "Josefin Sans", sans-serif; font-weight: 300;
    font-size: 24px; letter-spacing: 4px; line-height: 1;
  }
  .brand__tagline {
    font-family: "Josefin Sans", sans-serif; font-weight: 300;
    font-size: 10px; letter-spacing: 3px; margin-top: 6px;
  }
  .product {
    position: absolute; left: 34px; top: 138px;
  }
  .product__kind, .product__type {
    font-weight: 500; font-size: 25px; line-height: 1; text-transform: uppercase;
  }
  .product__type { margin-top: 10px; }
  .product__rule {
    position: absolute; left: 0; top: 162px;
    width: 228px; height: 2px; background: var(--ink);
  }
  .product__notes {
    position: absolute; left: 34px; top: 202px;
    font-size: 10.5px; line-height: 1.35; font-weight: 400;
  }
  .product__volume {
    position: absolute; right: 8px; top: 216px;
    font-size: 13px; font-weight: 500;
  }

  .label__info {
    width: 90px; padding: 26px 10px 0 2px;
    font-size: 5.5px; line-height: 1.35;
  }
  .info-block { margin-bottom: 10px; }
  .info-block__title { font-weight: 600; text-transform: uppercase; }
</style>
</head>
<body>
<main class="label-sheet">

  <article class="label label--mivo">
    <div class="label__front">
      <div class="brand">
        <span class="brand__dot"></span>
        <div class="brand__text">
          <span class="brand__name">TOLVAREN</span>
          <span class="brand__tagline">NATURAL SKINCARE</span>
        </div>
      </div>
      <div class="product">
        <h2 class="product__kind">Mivo</h2>
        <h3 class="product__type">Body Butter</h3>
      </div>
      <div class="product__rule"></div>
      <p class="product__notes">Guarana &amp; Cupuaçu Butter<br>(inspired By Brazil)</p>
      <p class="product__volume">200 ml</p>
    </div>
    <div class="label__info">
      <p class="info-block"><span class="info-block__title">Ingredients:</span> Shea butter, cupuaçu butter, guarana extract, natural oils.</p>
      <p class="info-block"><span class="info-block__title">Application:</span> Massage gently onto clean skin until fully absorbed.</p>
      <p class="info-block"><span class="info-block__title">Product instructions:</span> Store in a cool dry place away from sunlight. Use within twelve months of opening.</p>
      <p class="info-block"><span class="info-block__title">Warning:</span> For external use only. Avoid contact with eyes. Patch test before use.</p>
    </div>
  </article>

  <article class="label label--honey">
    <div class="label__front">
      <div class="brand">
        <span class="brand__dot"></span>
        <div class="brand__text">
          <span class="brand__name">TOLVAREN</span>
          <span class="brand__tagline">NATURAL SKINCARE</span>
        </div>
      </div>
      <div class="product">
        <h2 class="product__kind">Manuka Honey</h2>
        <h3 class="product__type">Body Butter</h3>
      </div>
      <div class="product__rule"></div>
      <p class="product__notes">Manuka honey (from New Zealand)<br>&amp; Cupuaçu butter.</p>
      <p class="product__volume">200 ml</p>
    </div>
    <div class="label__info">
      <p class="info-block"><span class="info-block__title">Ingredients:</span> Shea butter, manuka honey, cupuaçu butter, natural oils.</p>
      <p class="info-block"><span class="info-block__title">Application:</span> Massage gently onto clean skin until fully absorbed.</p>
      <p class="info-block"><span class="info-block__title">Product instructions:</span> Store in a cool dry place away from sunlight. Use within twelve months of opening.</p>
      <p class="info-block"><span class="info-block__title">Warning:</span> For external use only. Avoid contact with eyes. Patch test before use.</p>
    </div>
  </article>

  <article class="label label--coffee">
    <div class="label__front">
      <div class="brand">
        <span class="brand__dot"></span>
        <div class="brand__text">
          <span class="brand__name">TOLVAREN</span>
          <span class="brand__tagline">NATURAL SKINCARE</span>
        </div>
      </div>
      <div class="product">
        <h2 class="product__kind">Coffee</h2>
        <h3 class="product__type">Body Scrub</h3>
      </div>
      <div class="product__rule"></div>
      <p class="product__notes">Coffee and Demerara sugar</p>
      <p class="product__volume">200 ml</p>
    </div>
    <div class="label__info">
      <p class="info-block"><span class="info-block__title">Ingredients:</span> Ground coffee, demerara sugar, coconut oil, natural oils.</p>
      <p class="info-block"><span class="info-block__title">Application:</span> Massage gently onto clean skin until fully absorbed.</p>
      <p class="info-block"><span class="info-block__title">Product instructions:</span> Store in a cool dry place away from sunlight. Use within twelve months of opening.</p>
      <p class="info-block"><span class="info-block__title">Warning:</span> For external use only. Avoid contact with eyes. Patch test before use.</p>
    </div>
  </article>

</main>
</body>
</html>
```